Brightleaf Notes

We need two websites: both are already online, using Drupal.
I would prefer to use Drupal for both, so if you know nothing about Drupal, or wld prefer to use Wordpress please don't submit a proposal.
One website will be a blog. The domain is brightleafnotes.com.
For this site, we need to be able to post blogs; take comments; invite members; perhaps send out a weekly newsletter; and perhaps introduce weekly interactive elements e.g. a poll.
The other website is to house a new company. The domain is tkmpower.com.
This would also be very simple, allowing for administrator and third party posts and blogs, and interactive elements such as forums.
Neither project is ambitious; the priority is a simple to use, attractive, professional looking shop window.
Updates

i havent had much interest in this web design and coding project; am therefore happy to make brief the project easier/ better value - i need coding, and that is included in the fee. but am happy to limit this to home page for one website; we can negotiate a higher fee for an additional home page for another website; and i am happy if you work in wordpress or other; i prefer drupal simply because that is the template we are using at present. in addition i am happy to guarantee the project for the right designer, if thats a priority

Reason: project extended just to give us time to make a decision on Monday/ Tuesday !

Industry/Entity Type

Online

Coding

Coded - Design and coding required

```html
<!DOCTYPE html>
<html lang="en">
<head>
<meta charset="utf-8">
<title>Brightleaf Notes</title>
<link href="https://fonts.googleapis.com/css2?family=Bebas+Neue&family=Open+Sans:wght@400;600;700&family=Titillium+Web:wght@400;600&display=swap" rel="stylesheet">
<style>
:root{
  --orange:#e06b12;
  --orange-dark:#c95d0c;
  --ink:#1e1e1e;
  --text:#4a4a4a;
  --muted:#9a9a9a;
  --line:#d6d6d6;
  --panel:#efefef;
  --dark:#3a3a3a;
  --feed:#2fb3cf;
  --black:#0d0d0d;
  --white:#ffffff;
}
*{box-sizing:border-box;margin:0;padding:0}
html,body{width:1200px;height:2624px;overflow:hidden;background:var(--white)}
body{position:relative;font-family:"Open Sans",Arial,sans-serif;color:var(--text)}

/* header */
.site-header{position:absolute;left:0;top:0;width:1200px;height:126px;background:var(--white)}
.brand{position:absolute;left:98px;top:26px;display:flex;align-items:center;gap:18px}
.brand-mark{font-family:"Titillium Web",sans-serif;font-size:56px;font-weight:400;color:var(--orange);line-height:1}
.brand-name{font-family:"Titillium Web",sans-serif;font-size:25px;color:var(--ink);line-height:1.1}
.brand-tag{font-size:11px;font-style:italic;color:#666;margin-top:2px}
.main-nav{position:absolute;left:780px;top:42px;display:flex;align-items:center;gap:34px;font-size:13px;color:var(--ink)}
.main-nav .active{background:var(--orange);color:var(--white);width:91px;height:42px;border-radius:3px;display:flex;align-items:center;justify-content:center;font-weight:600}

/* slider */
.hero{position:absolute;left:0;top:126px;width:1200px;height:544px}
.hero-photo{position:absolute;inset:0;background:linear-gradient(180deg,#58656b 0%,#717d7e 45%,#86837b 75%,#85786a 100%)}
.hero-title{position:absolute;left:96px;top:222px;font-family:"Titillium Web",sans-serif;font-size:36px;font-weight:400;color:var(--white)}
.hero-arrow{position:absolute;top:232px;width:34px;height:34px;border-radius:50%;background:var(--white);border:2px solid #cfcfcf;display:flex;align-items:center;justify-content:center}
.hero-arrow.prev{left:38px}.hero-arrow.next{left:1120px}
.hero-dots{position:absolute;left:576px;top:500px;display:flex;gap:8px}
.hero-dots span{width:14px;height:14px;border-radius:50%;background:var(--white);border:2px solid #bbb}
.hero-dots .on{background:var(--orange);border-color:#f3b27c}

/* welcome */
.welcome{position:absolute;left:119px;top:690px;width:965px;text-align:center}
.welcome h1{font-family:"Bebas Neue",sans-serif;font-weight:400;font-size:44px;color:var(--ink);letter-spacing:.5px}
.welcome h1 span{color:var(--orange)}
.welcome p{font-size:11.9px;line-height:23.6px;color:#555;margin-top:4px}

.section-title{position:absolute;left:100px;top:860px;font-family:"Bebas Neue",sans-serif;font-size:36px;font-weight:400;color:var(--ink)}

/* posts */
.posts{position:absolute;left:100px;top:915px;width:733px}
.post{height:502px}
.post-media{position:relative;height:227px;border:1px solid var(--line);padding:5px;background:var(--white)}
.post-photo{width:100%;height:100%}
.photo-sunset{background:linear-gradient(180deg,#2a2d3a 0%,#5a4a4a 45%,#c98a42 72%,#3a3418 82%,#2b3414 100%)}
.photo-plant{background:linear-gradient(180deg,#7a8088 0%,#9a9a98 35%,#6e6a62 65%,#4a4640 100%)}
.photo-towers{background:linear-gradient(180deg,#3b5a86 0%,#7d92ad 40%,#a5a39b 62%,#6c665c 85%,#8a6c4a 100%)}
.post-date{position:absolute;right:14px;bottom:12px;display:flex;align-items:flex-end;gap:2px;color:var(--white)}
.post-date b{font-family:"Bebas Neue",sans-serif;font-weight:400;font-size:46px;line-height:.85}
.post-date small{font-size:11px;line-height:1.15;font-weight:600}
.post-head{display:flex;justify-content:space-between;align-items:center;margin-top:18px}
.post-head h2{font-size:16px;font-weight:600;color:var(--ink)}
.rating{display:flex;gap:2px}
.post-body{font-size:10.4px;line-height:23.6px;color:#555;margin-top:8px}
.post-foot{display:flex;justify-content:space-between;align-items:center;margin-top:14px}
.read-more{font-family:"Bebas Neue",sans-serif;font-size:17px;color:var(--white);background:var(--orange);width:86px;height:35px;display:flex;align-items:center;justify-content:center;border-bottom:3px solid var(--orange-dark)}
.post-meta{display:flex;align-items:center;gap:14px;font-size:11px;font-style:italic;color:var(--ink)}

.pager{position:absolute;left:572px;top:2431px;display:flex;align-items:center;gap:11px}
.pager span{width:32px;height:32px;border:1px solid var(--line);display:flex;align-items:center;justify-content:center;font-size:13px;color:var(--ink);border-radius:2px}
.pager .on{background:var(--orange);color:var(--white);border-color:var(--orange)}
.pager i{width:0;height:0;border-top:7px solid transparent;border-bottom:7px solid transparent}
.pager .prev{border-right:11px solid #999}
.pager .next{border-left:11px solid var(--orange)}

/* sidebar */
.sidebar{position:absolute;left:857px;width:243px}
.search{top:892px;height:53px;border:1px solid var(--line);display:flex;align-items:center;justify-content:space-between;padding:0 12px;font-size:10px;color:#888}
.login{top:969px;height:168px;background:var(--orange);padding:12px 14px}
.widget-title{font-family:"Titillium Web",sans-serif;font-size:17px;font-weight:600;color:var(--white)}
.field{height:36px;background:var(--white);border:2px solid #f4c9a4;margin-top:8px;font-size:10px;color:#888;display:flex;align-items:center;padding:0 10px}
.btn-dark{background:var(--dark);color:var(--white);font-size:11px;font-weight:600;display:flex;align-items:center;justify-content:center;border-radius:3px}
.login .btn-dark{width:78px;height:30px;margin:8px 0 0 auto}
.poll{top:1168px;height:287px;border:1px solid var(--line)}
.poll .bar{background:var(--orange);height:44px;padding:0 14px;display:flex;align-items:center}
.poll-q{color:var(--orange);font-size:12px;padding:12px 14px 6px}
.poll ul{list-style:none;padding:0 14px}
.poll li{display:flex;align-items:center;gap:10px;font-size:12px;color:#aaa;height:31px}
.poll li.on{color:var(--ink)}
.poll li i{width:12px;height:12px;border-radius:50%;border:1px solid #ccc}
.poll .btn-dark{width:82px;height:29px;margin:6px 0 0 146px;font-weight:400}
.feed{top:1480px;height:351px;border:1px solid var(--line)}
.feed .bar{background:var(--feed);height:50px;padding:0 14px;display:flex;align-items:center;gap:10px}
.feed .bar b{font-family:"Titillium Web",sans-serif;font-size:17px;font-weight:600;color:var(--white)}
.tweet{margin:0 14px;padding:14px 0 10px;border-bottom:1px dashed #bbb}
.tweet:last-child{border:0}
.tweet-head{display:flex;gap:12px;align-items:flex-start}
.tweet-mark{font-family:"Titillium Web",sans-serif;font-size:30px;color:var(--orange);line-height:1;width:50px}
.tweet-name{font-size:11px;font-weight:600;color:var(--ink)}
.tweet-handle{font-size:10px;color:#666;margin-top:4px}
.tweet p{font-size:11px;line-height:20px;color:#555;margin-top:8px}
.tweet-acts{display:flex;justify-content:flex-end;gap:10px;margin-top:4px}
.social{top:1871px;height:163px;background:var(--panel);text-align:center;padding-top:16px}
.social h3{font-family:"Titillium Web",sans-serif;font-size:23px;font-weight:400;color:var(--ink)}
.social-row{display:flex;justify-content:center;gap:11px;margin-top:14px}
.social-row span{width:46px;height:46px;border-radius:7px}
.newsletter{top:2071px;height:364px;background:#e3e3e3}
.newsletter .bar{background:var(--orange);height:45px;padding:0 14px;display:flex;align-items:center}
.newsletter .field{margin:18px 14px 0;height:35px;border:1px solid #ccc}
.newsletter .msg{height:130px;align-items:flex-start;padding-top:10px}
.newsletter .btn-dark{width:120px;height:35px;margin:14px 0 0 14px;justify-content:space-between;padding:0 14px;font-weight:400;font-size:13px;border-radius:2px}

/* footer */
.site-footer{position:absolute;left:0;top:2520px;width:1200px;height:104px;background:var(--black);color:var(--white);font-size:11px}
.footer-links{position:absolute;left:98px;top:32px}
.footer-copy{position:absolute;left:98px;top:56px}
.footer-social{position:absolute;left:977px;top:44px;display:flex;gap:7px}
.footer-social span{width:23px;height:23px;border-radius:3px}
</style>
</head>
<body>

<header class="site-header">
  <div class="brand">
    <div class="brand-mark">bn</div>
    <div>
      <div class="brand-name">Brightleaf Notes</div>
      <div class="brand-tag">Intelligent comment, from Martin Hale and Owen Pryce</div>
    </div>
  </div>
  <nav class="main-nav">
    <span class="active">Home</span><span>About Us</span><span>Blog</span><span>Contatc Us</span>
  </nav>
</header>

<section class="hero">
  <div class="hero-photo" role="img" aria-label="Slide image: a hazy sky backdrop with an illustrated globe showing green countryside above and polluting industry below"></div>
  <h2 class="hero-title">Brightleaf Notes</h2>
  <span class="hero-arrow prev"><svg width="12" height="14"><path d="M9 1 3 7l6 6" stroke="#333" stroke-width="3" fill="none"/></svg></span>
  <span class="hero-arrow next"><svg width="12" height="14"><path d="M3 1l6 6-6 6" stroke="#333" stroke-width="3" fill="none"/></svg></span>
  <div class="hero-dots"><span class="on"></span><span></span><span></span></div>
</section>

<section class="welcome">
  <h1>Welcome to <span>BN</span></h1>
  <p>Lorem ipsum dolor sit amet, consectetuer adipiscing elit, sed diam nonummy nibh euismod tincidunt ut laoreet dolore magna aliquam erat volutpat. Ut wisi enim ad minim veniam, quis nostrud exerci tation ullamcorper suscipit lobortis nisl ut aliquip ex ea commodo consequat. Lorem ipsum dolor sit amet, consectetuer adipiscing elit, sed diam nonummy nibh euismod tincidunt ut laoreet dolore magna aliquam erat volutpat. Ut wisi enim ad minim veniam, quis nostrud exerci tation ullamcorper suscipit lobortis nisl ut aliquip ex ea commodo consequat.</p>
</section>

<h2 class="section-title">Blog</h2>

<svg width="0" height="0" style="position:absolute">
  <defs>
    <polygon id="star" points="9,1 11.4,6.5 17,7 12.7,10.8 14,16.5 9,13.5 4,16.5 5.3,10.8 1,7 6.6,6.5"/>
  </defs>
</svg>

<main class="posts">
  <article class="post">
    <div class="post-media">
      <div class="post-photo photo-sunset" role="img" aria-label="Wind turbines silhouetted against a sunset over a field"></div>
      <div class="post-date"><b>09</b><small>Nov<br>2014</small></div>
    </div>
    <div class="post-head"><h2>Paradox of European power prices...</h2>
      <div class="rating"><svg width="18" height="18" fill="#f4b400"><use href="#star"/></svg><svg width="18" height="18" fill="#f4b400"><use href="#star"/></svg><svg width="18" height="18" fill="#f4b400"><use href="#star"/></svg><svg width="18" height="18" fill="#d0d0d0"><use href="#star"/></svg><svg width="18" height="18" fill="#d0d0d0"><use href="#star"/></svg></div>
    </div>
    <p class="post-body">Power prices is not an easy topic to talk about. First and foremost, there are lots of different power prices from baseload to peak, from wholesale to retail, from heavy industry to commercial prices. And each country across Europe has different prices and then there are renewables pushing up the power prices, or so they say. Then we have the European Union with their goal of making energy "affordable, competitively priced, environmentally sustainable and secure for everybody." And how are they doing this. Power prices is not an easy topic to talk about. First and foremost, there are lots of different power prices from baseload to peak, from wholesale to retail, from heavy industry to commercial prices. And each country across .</p>
    <div class="post-foot"><span class="read-more">Read More</span>
      <div class="post-meta">
        <svg width="16" height="14"><path d="M7 2 1 7l6 5V9c4 0 6 1 8 4 0-5-3-8-8-8z" fill="#888"/></svg>
        <svg width="18" height="14"><path d="M4 3h9v5h2l-3 4-3-4h2V5H6v2H2zM2 3l2-2 2 2" fill="#888"/></svg>
        <svg width="16" height="16" fill="#888"><use href="#star"/></svg>
        <span>- Submitted by Martinhale</span>
      </div>
    </div>
  </article>

  <article class="post">
    <div class="post-media">
      <div class="post-photo photo-plant" role="img" aria-label="Industrial power plant with large pipes and steel structures"></div>
      <div class="post-date"><b>09</b><small>Nov<br>2014</small></div>
    </div>
    <div class="post-head"><h2>Paradox of European power prices...</h2>
      <div class="rating"><svg width="18" height="18" fill="#f4b400"><use href="#star"/></svg><svg width="18" height="18" fill="#f4b400"><use href="#star"/></svg><svg width="18" height="18" fill="#f4b400"><use href="#star"/></svg><svg width="18" height="18" fill="#d0d0d0"><use href="#star"/></svg><svg width="18" height="18" fill="#d0d0d0"><use href="#star"/></svg></div>
    </div>
    <p class="post-body">Power prices is not an easy topic to talk about. First and foremost, there are lots of different power prices from baseload to peak, from wholesale to retail, from heavy industry to commercial prices. And each country across Europe has different prices and then there are renewables pushing up the power prices, or so they say. Then we have the European Union with their goal of making energy "affordable, competitively priced, environmentally sustainable and secure for everybody." And how are they doing this. Power prices is not an easy topic to talk about. First and foremost, there are lots of different power prices from baseload to peak, from wholesale to retail, from heavy industry to commercial prices. And each country across .</p>
    <div class="post-foot"><span class="read-more">Read More</span>
      <div class="post-meta">
        <svg width="16" height="14"><path d="M7 2 1 7l6 5V9c4 0 6 1 8 4 0-5-3-8-8-8z" fill="#888"/></svg>
        <svg width="18" height="14"><path d="M4 3h9v5h2l-3 4-3-4h2V5H6v2H2zM2 3l2-2 2 2" fill="#888"/></svg>
        <svg width="16" height="16" fill="#888"><use href="#star"/></svg>
        <span>- Submitted by Martinhale</span>
      </div>
    </div>
  </article>

  <article class="post">
    <div class="post-media">
      <div class="post-photo photo-towers" role="img" aria-label="Coal power station with cooling towers and chimneys under a cloudy sky"></div>
      <div class="post-date"><b>09</b><small>Nov<br>2014</small></div>
    </div>
    <div class="post-head"><h2>Paradox of European power prices...</h2>
      <div class="rating"><svg width="18" height="18" fill="#f4b400"><use href="#star"/></svg><svg width="18" height="18" fill="#f4b400"><use href="#star"/></svg><svg width="18" height="18" fill="#f4b400"><use href="#star"/></svg><svg width="18" height="18" fill="#d0d0d0"><use href="#star"/></svg><svg width="18" height="18" fill="#d0d0d0"><use href="#star"/></svg></div>
    </div>
    <p class="post-body">Power prices is not an easy topic to talk about. First and foremost, there are lots of different power prices from baseload to peak, from wholesale to retail, from heavy industry to commercial prices. And each country across Europe has different prices and then there are renewables pushing up the power prices, or so they say. Then we have the European Union with their goal of making energy "affordable, competitively priced, environmentally sustainable and secure for everybody." And how are they doing this. Power prices is not an easy topic to talk about. First and foremost, there are lots of different power prices from baseload to peak, from wholesale to retail, from heavy industry to commercial prices. And each country across .</p>
    <div class="post-foot"><span class="read-more">Read More</span>
      <div class="post-meta">
        <svg width="16" height="14"><path d="M7 2 1 7l6 5V9c4 0 6 1 8 4 0-5-3-8-8-8z" fill="#888"/></svg>
        <svg width="18" height="14"><path d="M4 3h9v5h2l-3 4-3-4h2V5H6v2H2zM2 3l2-2 2 2" fill="#888"/></svg>
        <svg width="16" height="16" fill="#888"><use href="#star"/></svg>
        <span>- Submitted by Martinhale</span>
      </div>
    </div>
  </article>
</main>

<nav class="pager"><i class="prev"></i><span class="on">1</span><span>2</span><span>3</span><span>4</span><span>5</span><i class="next"></i></nav>

<aside>
  <div class="sidebar search">Search
    <svg width="16" height="16"><circle cx="7" cy="7" r="5" stroke="#555" stroke-width="1.6" fill="none"/><path d="M11 11l4 4" stroke="#555" stroke-width="1.8"/></svg>
  </div>

  <div class="sidebar login">
    <div class="widget-title">LOGIN</div>
    <div class="field">User name</div>
    <div class="field">***********</div>
    <div class="btn-dark">Send</div>
  </div>

  <div class="sidebar poll">
    <div class="bar"><span class="widget-title">Today Poll</span></div>
    <div class="poll-q">Paradox of European power prices</div>
    <ul>
      <li class="on"><svg width="12" height="12"><circle cx="6" cy="6" r="6" fill="#3bb54a"/><path d="M3 6l2 2 4-4" stroke="#fff" stroke-width="1.6" fill="none"/></svg>Paradox of European power</li>
      <li><i></i>The Nuclear Renaissance</li>
      <li><i></i>The Nuclear Renaissance</li>
      <li><i></i>The Nuclear Renaissance</li>
      <li><i></i>The Nuclear Renaissance</li>
    </ul>
    <div class="btn-dark">Vote</div>
  </div>

  <div class="sidebar feed">
    <div class="bar"><svg width="16" height="16"><circle cx="8" cy="8" r="7" fill="#fff"/></svg><b>Feed</b></div>
    <div class="tweet">
      <div class="tweet-head"><span class="tweet-mark">bn</span><div><div class="tweet-name">Brightleaf Notes</div><div class="tweet-handle">@BRIGHTLEAF</div></div></div>
      <p>We just improved our search; get fast and more accurate results.</p>
      <div class="tweet-acts">
        <svg width="14" height="12"><path d="M6 1 1 6l5 5V8c3 0 5 1 7 3 0-4-3-7-7-7z" fill="#999"/></svg>
        <svg width="16" height="12"><path d="M4 2h8v4h2l-3 4-3-4h2V4H6v2H2z" fill="#999"/></svg>
        <svg width="14" height="14" fill="#999"><use href="#star"/></svg>
      </div>
    </div>
    <div class="tweet">
      <div class="tweet-head"><span class="tweet-mark">bn</span><div><div class="tweet-name">Brightleaf Notes</div><div class="tweet-handle">@BRIGHTLEAF</div></div></div>
      <p>We just improved our search; get fast and more accurate results.</p>
      <div class="tweet-acts">
        <svg width="14" height="12"><path d="M6 1 1 6l5 5V8c3 0 5 1 7 3 0-4-3-7-7-7z" fill="#999"/></svg>
        <svg width="16" height="12"><path d="M4 2h8v4h2l-3 4-3-4h2V4H6v2H2z" fill="#999"/></svg>
        <svg width="14" height="14" fill="#999"><use href="#star"/></svg>
      </div>
    </div>
  </div>

  <div class="sidebar social">
    <h3>Social</h3>
    <div class="social-row">
      <span style="background:#3b5a98"></span><span style="background:#3aa3dc"></span><span style="background:#19b3e6"></span><span style="background:#e0505f"></span>
    </div>
  </div>

  <div class="sidebar newsletter">
    <div class="bar"><span class="widget-title">Newsletter Signup</span></div>
    <div class="field">Name</div>
    <div class="field">Your email address</div>
    <div class="field msg">Message</div>
    <div class="btn-dark">Send it <svg width="22" height="10"><path d="M0 5h20M15 1l5 4-5 4" stroke="#fff" fill="none"/></svg></div>
  </div>
</aside>

<footer class="site-footer">
  <div class="footer-links">Home &nbsp;|&nbsp; About Us &nbsp;|&nbsp; Products &nbsp;|&nbsp; Contact Us</div>
  <div class="footer-copy">© 2014 Company Name &nbsp;All right reserved &nbsp;Term of Use</div>
  <div class="footer-social">
    <span style="background:#3b5a98"></span><span style="background:#3aa3dc"></span><span style="background:#1a77b5"></span><span style="background:#f08a1c"></span>
  </div>
</footer>

</body>
</html>
```